design a construction company business card

Design business card around our logo. Card must have all the typical info: name, title, address, phone, email, business name, etc. Somewhere on the card I would like to see our motto "Built with care... Driven by dedication." Consider adding a splash of bright orange to the card to complement the blues and silvers/grays in the logo. We are open to metallic inks, textures, etc. We would like to see options on both light and dark backgrounds. The font in the logo is Euro Technic Extended Regular.

```html
<!DOCTYPE html>
<html lang="en">
<head>
<meta charset="utf-8">
<title>Halden Contracting – Business Card</title>
<link href="https://fonts.googleapis.com/css2?family=Michroma&family=Exo+2:wght@400;700;800&display=swap" rel="stylesheet">
<style>
  :root{
    --stage:#4b4b4e;
    --card-top:#333335;
    --card-bottom:#242426;
    --blue:#1f6fc6;
    --blue-bright:#2a86e0;
    --silver:#8d8f94;
    --text:#c4c5c8;
    --icon-cut:#2a2a2c;
    --name-font:"Michroma", sans-serif;
    --body-font:"Exo 2", sans-serif;
  }
  *{margin:0;padding:0;box-sizing:border-box}
  html,body{width:1200px;height:1000px;overflow:hidden}
  body{background:var(--stage);position:relative;font-family:var(--body-font);color:var(--text)}
  .card{
    position:absolute;width:700px;height:400px;border-radius:26px;overflow:hidden;
    background:linear-gradient(160deg,var(--card-top),var(--card-bottom));
  }
  .card-front{left:440px;top:50px}
  .card-back{left:60px;top:530px}

  /* front */
  .front-brand{position:absolute;left:0;right:0;top:120px;text-align:center}
  .brand-name{font-family:var(--name-font);color:var(--blue);font-size:66px;letter-spacing:4px;line-height:1}
  .brand-sub{font-family:var(--name-font);color:var(--silver);font-size:19px;letter-spacing:2px;margin-top:14px}
  .motto{position:absolute;left:0;right:0;top:300px;text-align:center;color:var(--blue-bright);
    font-family:var(--body-font);font-weight:800;font-size:17px;letter-spacing:1.6px}

  /* back */
  .back-brand{position:absolute;left:42px;top:70px}
  .back-brand .brand-name{font-size:48px;letter-spacing:3px}
  .back-brand .brand-sub{font-size:14px;margin-top:10px}
  .divider{position:absolute;left:42px;top:195px;width:430px;height:2px;background:var(--blue)}
  .address{position:absolute;left:42px;top:212px;font-size:18px;line-height:25px;color:var(--text)}
  .address .phone{display:flex;align-items:center;gap:6px}
  .contact{position:absolute;right:48px;top:200px;text-align:right}
  .person-name{font-family:var(--body-font);font-weight:800;font-size:27px;color:var(--blue-bright);letter-spacing:1px}
  .person-title{font-size:19px;margin-top:2px}
  .contact-line{display:flex;justify-content:flex-end;align-items:center;gap:7px;font-size:18px;margin-top:4px}
  .contact-line.first{margin-top:10px}
  .icon{width:14px;height:14px;flex:none}
  .band{position:absolute;left:0;bottom:0;width:700px;height:80px}
</style>
</head>
<body>

<section class="card card-front">
  <div class="front-brand">
    <div class="brand-name">HALDEN</div>
    <div class="brand-sub">— CONTRACTING, INC. —</div>
  </div>
  <p class="motto">BUILT WITH CARE... DRIVEN BY DEDICATION.</p>
</section>

<section class="card card-back">
  <div class="back-brand">
    <div class="brand-name">HALDEN</div>
    <div class="brand-sub">— CONTRACTING, INC. —</div>
  </div>
  <div class="divider"></div>

  <div class="address">
    <div>482 Harbor Avenue N.Y.</div>
    <div>Brookvale AB 7TR</div>
    <div class="phone">
      <svg class="icon" viewBox="0 0 16 16"><path fill="var(--blue-bright)" d="M3.5 1l2.5 3-1.5 2c1 2 3 4 5 5l2-1.5 3 2.5-1.5 2.5C8 15 1 8 1 2.5z"/></svg>
      <span>500.014.2200</span>
    </div>
  </div>

  <div class="contact">
    <div class="person-name">Daniel Reyes</div>
    <div class="person-title">Managing Director</div>
    <div class="contact-line first">
      <svg class="icon" viewBox="0 0 16 16"><rect x="1" y="3" width="14" height="10" rx="1.5" fill="var(--blue-bright)"/><path d="M1.5 4l6.5 5 6.5-5" stroke="var(--icon-cut)" stroke-width="1.4" fill="none"/></svg>
      <span>daniel@haldenbuild.com</span>
    </div>
    <div class="contact-line">
      <svg class="icon" viewBox="0 0 16 16"><circle cx="8" cy="8" r="7" fill="var(--blue-bright)"/><path d="M1 8h14M8 1c-3 3-3 11 0 14M8 1c3 3 3 11 0 14" stroke="var(--icon-cut)" stroke-width="1.1" fill="none"/></svg>
      <span>www.haldenbuild.com</span>
    </div>
  </div>

  <svg class="band" viewBox="0 0 700 80" preserveAspectRatio="none" aria-hidden="true">
    <path d="M0 20 L452 30 L446 38 L0 28 Z" fill="var(--silver)"/>
    <path d="M0 30 L450 40 C468 40 478 14 500 14 L700 14 L700 80 L0 80 Z" fill="var(--blue)"/>
  </svg>
</section>

</body>
</html>
```